New Business Card Design Project

Target Market(s)

Passing cards out

Industry/Entity Type

Asphalt contractor

Contact Information for Business Card

Ridgefold Paving

Colors
FFC000
F8CF3A
FAE287
FDF2CF
FEFAEE
F0912C
F2A743
F7CA91
FBE8D2
FDF5EE
EE7325
F08F49
F5BC92
FAE3D3
FDF4ED

Requirements
Must have
• Asphalt
Nice to have
• Would like to have 2 pictures on it of equipment

```html
<!DOCTYPE html>
<html lang="en">
<head>
<meta charset="utf-8">
<title>Ridgefold Paving – Business Card</title>
<link rel="stylesheet" href="https://fonts.googleapis.com/css2?family=Montserrat:wght@500;700;800&display=swap">
<style>
  :root {
    --page: #e6e6e6;
    --card: #ffffff;
    --brand-orange: #ee7325;
    --brand-amber: #f0912c;
    --line-yellow: #ffc000;
    --ink: #1a1a1a;
    --asphalt-light: #f6f6f6;
    --asphalt-mid: #8a8a8a;
    --asphalt-dark: #4a4a4a;
    --shadow: rgba(0, 0, 0, 0.22);
  }
  * { box-sizing: border-box; margin: 0; padding: 0; }
  html, body {
    width: 1200px; height: 1200px; overflow: hidden;
    background: var(--page);
    font-family: "Montserrat", Arial, sans-serif;
    color: var(--ink);
  }
  .canvas { position: relative; width: 1200px; height: 1200px; }
  .card {
    position: absolute; left: 228px; width: 742px; height: 436px;
    background: var(--card);
    box-shadow: 4px 6px 14px var(--shadow);
    overflow: hidden;
  }
  .card--front { top: 121px; }
  .card--back { top: 643px; }

  .road-scene {
    position: absolute; inset: 0;
    background: linear-gradient(180deg,
      var(--asphalt-light) 0%, var(--asphalt-light) 40%,
      #cfcfcf 56%, var(--asphalt-mid) 76%, var(--asphalt-dark) 100%);
  }
  .road-line {
    position: absolute; bottom: 0; width: 8px; height: 70px;
    background: var(--line-yellow); opacity: 0.75;
  }
  .road-line--left { left: 360px; }
  .road-line--right { left: 376px; }
  .brand-name {
    position: absolute; left: 0; right: 0; top: 62px;
    text-align: center;
    font-weight: 800; font-size: 70px; line-height: 76px;
    color: var(--brand-orange);
  }
  .brand-dot {
    position: absolute; left: 315px; top: 236px;
    width: 120px; height: 120px; border-radius: 50%;
    background: var(--brand-orange);
  }
  .equipment {
    position: absolute; top: 266px; width: 190px; height: 96px;
    background: var(--brand-amber); border-radius: 6px;
  }
  .equipment--paver { left: 47px; }
  .equipment--truck { left: 507px; }

  .contact-name {
    position: absolute; left: 49px; top: 42px;
    font-weight: 700; font-size: 60px; line-height: 1;
    color: var(--brand-orange);
  }
  .contact-title {
    position: absolute; left: 50px; top: 116px;
    font-weight: 500; font-size: 27px;
  }
  .contact-rule {
    position: absolute; left: 49px; top: 164px;
    width: 644px; height: 3px; background: var(--brand-orange);
  }
  .contact-list { position: absolute; left: 49px; top: 190px; list-style: none; }
  .contact-item {
    display: flex; align-items: flex-start; gap: 14px;
    font-weight: 500; font-size: 26px; line-height: 36px;
    margin-bottom: 10px;
  }
  .contact-item svg { flex: none; width: 26px; height: 26px; margin-top: 5px; fill: var(--ink); }
  .contact-item--web { font-weight: 700; }
</style>
</head>
<body>
<main class="canvas">
  <section class="card card--front" aria-label="Card front">
    <div class="road-scene" role="img" aria-label="Asphalt road receding into fog"></div>
    <div class="road-line road-line--left" aria-hidden="true"></div>
    <div class="road-line road-line--right" aria-hidden="true"></div>
    <h1 class="brand-name">Ridgefold<br>Paving</h1>
    <div class="brand-dot" aria-hidden="true"></div>
    <div class="equipment equipment--paver" role="img" aria-label="Asphalt paving machine"></div>
    <div class="equipment equipment--truck" role="img" aria-label="Dump truck with raised bed"></div>
  </section>

  <section class="card card--back" aria-label="Card back">
    <h2 class="contact-name">Dale Harper</h2>
    <p class="contact-title">Project Manager</p>
    <div class="contact-rule"></div>
    <ul class="contact-list">
      <li class="contact-item">
        <svg viewBox="0 0 24 24" aria-hidden="true"><path d="M6.6 10.8a15.1 15.1 0 0 0 6.6 6.6l2.2-2.2a1 1 0 0 1 1-.25 11.4 11.4 0 0 0 3.6.57 1 1 0 0 1 1 1V20a1 1 0 0 1-1 1A17 17 0 0 1 3 4a1 1 0 0 1 1-1h3.5a1 1 0 0 1 1 1c0 1.25.2 2.45.57 3.57a1 1 0 0 1-.25 1z"/></svg>
        <span>Phone: (555) 204-6618</span>
      </li>
      <li class="contact-item">
        <svg viewBox="0 0 24 24" aria-hidden="true"><path d="M2 5h20v14H2zm2 2v.5l8 5 8-5V7zm0 2.8V17h16V9.8l-8 5z"/></svg>
        <span>Email: dale@ridgefoldpaving.com</span>
      </li>
      <li class="contact-item">
        <svg viewBox="0 0 24 24" aria-hidden="true"><path d="M12 2a7 7 0 0 0-7 7c0 5.2 7 13 7 13s7-7.8 7-13a7 7 0 0 0-7-7zm0 9.5A2.5 2.5 0 1 1 12 6.5a2.5 2.5 0 0 1 0 5z"/></svg>
        <span>Address: 2215 Quarry Lane,<br>Brookhaven, IL 62891</span>
      </li>
      <li class="contact-item contact-item--web">
        <svg viewBox="0 0 24 24" aria-hidden="true"><path d="M12 2a10 10 0 1 0 0 20 10 10 0 0 0 0-20zm6.9 9h-3a15 15 0 0 0-1.3-5.6A8 8 0 0 1 18.9 11zM12 4.1c.9 1.2 1.8 3.6 1.9 6.9h-3.8c.1-3.3 1-5.7 1.9-6.9zM9.4 5.4A15 15 0 0 0 8.1 11h-3a8 8 0 0 1 4.3-5.6zM5.1 13h3a15 15 0 0 0 1.3 5.6A8 8 0 0 1 5.1 13zm6.9 6.9c-.9-1.2-1.8-3.6-1.900-6.9h3.8c-.1 3.3-1 5.7-1.9 6.9zm2.6-1.3a15 15 0 0 0 1.3-5.6h3a8 8 0 0 1-4.3 5.6z"/></svg>
        <span>www.ridgefoldpaving.com</span>
      </li>
    </ul>
  </section>
</main>
</body>
</html>
```